Email Signature & Facebook Cover Design – Birchlane Study Centre

I’m looking for a clean, professional email signature and a matching Facebook cover photo for my tutoring business, Birchlane Study Centre.
The email signature needs to display properly across Outlook and iPhone without the image appearing as an attachment. It should include my logo and contact details and have a friendly but professional look suitable for an education business.
Details to include:
Moira Dunholt
Director & Lead Tutor
Birchlane Study Centre
hello@birchlanestudy.co.uk
www.birchlanestudy.co.uk
01632 418736
The Facebook cover should match the branding, feel professional and welcoming, and be optimised for desktop and mobile.

```html
<!DOCTYPE html>
<html lang="en">
<head>
<meta charset="utf-8">
<title>Birchlane Study Centre – Email Signature &amp; Facebook Cover</title>
<link rel="stylesheet" href="https://fonts.googleapis.com/css2?family=Poppins:wght@500;600;700;800&display=swap">
<style>
  :root {
    --board: #2a2a2a;
    --paper: #ffffff;
    --green: #4cba66;
    --ink: #1c1c1c;
    --label: #f2f2f2;
  }
  * { margin: 0; padding: 0; box-sizing: border-box; }
  html, body { width: 1200px; height: 292px; overflow: hidden; background: var(--board); }
  body { font-family: "Poppins", sans-serif; color: var(--ink); position: relative; }

  .panel { position: absolute; top: 27px; height: 200px; background: var(--paper); overflow: hidden; }
  .panel--signature { left: 25px; width: 601px; }
  .panel--cover { left: 640px; width: 534px; }

  .brand-name {
    position: absolute; text-align: center;
    font-weight: 800; color: var(--ink); line-height: 1.05;
  }
  .panel--signature .brand-name { left: 74px; width: 136px; top: 40px; font-size: 22px; }
  .panel--cover .brand-name { left: 238px; width: 90px; top: 26px; font-size: 13px; }
  .brand-dot { display: block; margin: 0 auto 6px; border-radius: 50%; background: var(--green); }
  .panel--signature .brand-dot { width: 16px; height: 16px; }
  .panel--cover .brand-dot { width: 10px; height: 10px; margin-bottom: 4px; }

  .name-badge {
    position: absolute; background: var(--green); color: #fff;
    font-weight: 800; text-transform: uppercase; border-radius: 2px;
    display: flex; align-items: center; justify-content: center; white-space: nowrap;
  }
  .panel--signature .name-badge { left: 71px; top: 141px; width: 141px; height: 17px; font-size: 10px; letter-spacing: 3.6px; }
  .panel--cover .name-badge { left: 336px; top: 21px; width: 126px; height: 15px; font-size: 8.5px; letter-spacing: 3px; }

  .job-title { position: absolute; font-weight: 500; font-size: 8.5px; white-space: nowrap; }
  .panel--signature .job-title { left: 71px; width: 141px; top: 165px; text-align: center; }
  .panel--cover .job-title { left: 336px; top: 42px; font-size: 7.5px; }

  .divider { position: absolute; background: var(--green); }
  .panel--signature .divider { left: 254px; top: 27px; width: 2px; height: 146px; }
  .panel--cover .divider { left: 213px; top: 0; width: 3px; height: 81px; }

  .company-band {
    position: absolute; right: 0; background: var(--green); color: #fff;
    font-weight: 800; white-space: nowrap; display: flex; align-items: center;
  }
  .panel--signature .company-band { left: 281px; top: 53px; height: 33px; font-size: 21px; padding-left: 17px; }
  .panel--cover .company-band { left: 242px; top: 89px; height: 29px; font-size: 18px; padding-left: 15px; }

  .contact-list { position: absolute; list-style: none; }
  .panel--signature .contact-list { left: 291px; top: 97px; }
  .panel--cover .contact-list { left: 241px; top: 124px; }
  .contact-item { display: flex; align-items: center; font-weight: 600; white-space: nowrap; }
  .contact-item svg { flex: none; }
  .panel--signature .contact-item { font-size: 12px; height: 18px; }
  .panel--signature .contact-item svg { width: 9px; height: 9px; margin-right: 16px; }
  .panel--signature .contact-item--phone { font-size: 17px; font-weight: 700; height: 25px; }
  .panel--cover .contact-item { font-size: 10.5px; height: 16px; }
  .panel--cover .contact-item svg { width: 8px; height: 8px; margin-right: 14px; }
  .panel--cover .contact-item--phone { font-size: 15px; font-weight: 700; height: 22px; }

  .cover-photo {
    position: absolute; left: 0; top: 0; width: 210px; height: 200px;
    background: linear-gradient(180deg, #4cba66 0%, #4cba66 55%, #a7773f 100%);
  }

  .board-label {
    position: absolute; top: 250px; width: 400px; text-align: center;
    color: var(--label); font-weight: 500; font-size: 11px; letter-spacing: 8px;
  }
  .board-label--signature { left: 176px; }
  .board-label--cover { left: 743px; }
</style>
</head>
<body>
  <svg width="0" height="0" style="position:absolute">
    <defs>
      <symbol id="icon-phone" viewBox="0 0 24 24"><path fill="#4cba66" d="M6.6 10.8a15 15 0 0 0 6.6 6.6l2.2-2.2a1 1 0 0 1 1-.25 11.4 11.4 0 0 0 3.6.57 1 1 0 0 1 1 1V20a1 1 0 0 1-1 1A17 17 0 0 1 3 4a1 1 0 0 1 1-1h3.5a1 1 0 0 1 1 1c0 1.25.2 2.45.57 3.57a1 1 0 0 1-.25 1z"/></symbol>
      <symbol id="icon-mail" viewBox="0 0 24 24"><rect x="2" y="5" width="20" height="14" fill="#4cba66"/><path d="M2 5l10 8 10-8M2 19l7-7M22 19l-7-7" stroke="#fff" stroke-width="1.6" fill="none"/></symbol>
      <symbol id="icon-web" viewBox="0 0 24 24"><g fill="none" stroke="#4cba66" stroke-width="1.8"><circle cx="12" cy="12" r="10"/><ellipse cx="12" cy="12" rx="4.5" ry="10"/><path d="M2 12h20M4 7h16M4 17h16"/></g></symbol>
    </defs>
  </svg>

  <section class="panel panel--signature" aria-label="Email signature">
    <div class="brand-name"><span class="brand-dot"></span>Birchlane<br>Study<br>Centre</div>
    <div class="name-badge">Moira Dunholt</div>
    <div class="job-title">DIRECTOR &amp; LEAD TUTOR</div>
    <div class="divider"></div>
    <div class="company-band">BIRCHLANE STUDY CENTRE</div>
    <ul class="contact-list">
      <li class="contact-item contact-item--phone"><svg><use href="#icon-phone"/></svg>01632 418736</li>
      <li class="contact-item"><svg><use href="#icon-mail"/></svg>hello@birchlanestudy.co.uk</li>
      <li class="contact-item"><svg><use href="#icon-web"/></svg>www.birchlanestudy.co.uk</li>
    </ul>
  </section>

  <section class="panel panel--cover" aria-label="Facebook cover">
    <div class="cover-photo" role="img" aria-label="Photo of a smiling student holding a laptop on a green background"></div>
    <div class="divider"></div>
    <div class="brand-name"><span class="brand-dot"></span>Birchlane<br>Study<br>Centre</div>
    <div class="name-badge">Moira Dunholt</div>
    <div class="job-title">DIRECTOR &amp; LEAD TUTOR</div>
    <div class="company-band">BIRCHLANE STUDY CENTRE</div>
    <ul class="contact-list">
      <li class="contact-item contact-item--phone"><svg><use href="#icon-phone"/></svg>01632 418736</li>
      <li class="contact-item"><svg><use href="#icon-mail"/></svg>hello@birchlanestudy.co.uk</li>
      <li class="contact-item"><svg><use href="#icon-web"/></svg>www.birchlanestudy.co.uk</li>
    </ul>
  </section>

  <div class="board-label board-label--signature">EMAIL SIGNATURE</div>
  <div class="board-label board-label--cover">FACEBOOK COVER</div>
</body>
</html>
```